Business Stationery for Bramwell Oakes Recruitment Ltd
Marnie Thwaite
Cutting-Edge
Director
42 Quillmere Road
Teddington
Middlesex
KT4 9RW
marnie@bramwelloakes.co.uk
www.bramwelloakes.co.uk
Please use attached logo - I require the business card and company stationery - cutting edge design please

```html
<!DOCTYPE html>
<html lang="en">
<head>
<meta charset="utf-8">
<title>Bramwell Oakes Recruitment – Business Card</title>
<link rel="stylesheet" href="https://fonts.googleapis.com/css2?family=Cinzel:wght@400;600&family=Montserrat:wght@400;600&display=swap">
<style>
  :root {
    --navy: #2a2a86;
    --navy-deep: #1c1c62;
    --navy-light: #3c3ca6;
    --silver: #9a9aa4;
    --silver-light: #c9c9d0;
    --ink: #55555f;
    --paper: #ffffff;
    --backdrop: #eef0f3;
  }
  * { box-sizing: border-box; margin: 0; padding: 0; }
  html, body {
    width: 1200px; height: 980px; overflow: hidden;
    background: var(--backdrop);
  }
  .canvas {
    position: relative; width: 1200px; height: 980px;
    display: flex; flex-direction: column; align-items: center; justify-content: center; gap: 40px;
  }
  .card {
    position: relative; width: 700px; height: 420px;
    border-radius: 26px; overflow: hidden;
    box-shadow: 0 6px 20px rgba(20, 20, 60, 0.15);
  }
  .card-front { background: var(--paper); }
  .card-front .swoosh { position: absolute; inset: 0; width: 100%; height: 100%; }

  .brand { position: absolute; left: 48px; top: 44px; display: flex; align-items: flex-start; gap: 14px; }
  .brand-mark { width: 18px; height: 18px; background: var(--navy); margin-top: 6px; }
  .brand-name {
    font-family: 'Cinzel', serif; font-weight: 400; color: var(--navy);
    font-size: 27px; line-height: 1.05; letter-spacing: 2px;
  }
  .brand-tagline {
    font-family: 'Cinzel', serif; font-weight: 400; color: var(--silver);
    font-size: 15px; letter-spacing: 5px; margin-top: 6px;
  }

  .contact-list {
    position: absolute; left: 48px; top: 150px; list-style: none;
    font-family: 'Montserrat', sans-serif; font-size: 11.5px; color: var(--ink);
    letter-spacing: 0.6px;
  }
  .contact-list li { display: flex; align-items: center; gap: 9px; height: 19px; }
  .contact-list svg { width: 11px; height: 11px; fill: var(--navy); flex: none; }

  .holder {
    position: absolute; right: 42px; bottom: 32px; text-align: right;
    font-family: 'Montserrat', sans-serif; color: var(--paper);
  }
  .holder-name { font-weight: 600; font-size: 15px; letter-spacing: 3px; text-transform: uppercase; }
  .holder-role { font-weight: 400; font-size: 10px; letter-spacing: 3px; text-transform: uppercase; margin-top: 5px; color: var(--silver-light); }

  .card-back {
    background: radial-gradient(ellipse at 50% 40%, var(--navy-light) 0%, var(--navy) 55%, var(--navy-deep) 100%);
  }
  .back-web {
    position: absolute; left: 48px; top: 52px;
    font-family: 'Montserrat', sans-serif; font-size: 11px; letter-spacing: 4px;
    color: var(--silver-light); text-transform: uppercase;
  }
  .back-brand {
    position: absolute; inset: 0; display: flex; align-items: center; justify-content: center; gap: 18px;
  }
  .back-brand .brand-mark { width: 26px; height: 26px; background: var(--silver-light); margin-top: 0; }
  .back-brand .brand-name { color: var(--silver-light); font-size: 44px; letter-spacing: 4px; }
</style>
</head>
<body>
<main class="canvas">

  <section class="card card-front" aria-label="Business card front">
    <svg class="swoosh" viewBox="0 0 700 420" preserveAspectRatio="none" aria-hidden="true">
      <defs>
        <linearGradient id="band" x1="0" y1="0" x2="1" y2="1">
          <stop offset="0" stop-color="#3a3aa2"/>
          <stop offset="1" stop-color="#1e1e66"/>
        </linearGradient>
      </defs>
      <path d="M0,268 C200,345 470,365 700,318 L700,420 L0,420 Z" fill="url(#band)"/>
      <path d="M0,244 C210,325 470,345 700,296" fill="none" stroke="#9a9aa4" stroke-width="7"/>
      <path d="M0,228 C215,306 470,326 700,280" fill="none" stroke="#c9c9d0" stroke-width="2"/>
    </svg>

    <div class="brand">
      <span class="brand-mark"></span>
      <div>
        <div class="brand-name">Bramwell Oakes</div>
        <div class="brand-tagline">Recruitment</div>
      </div>
    </div>

    <ul class="contact-list">
      <li><svg viewBox="0 0 12 12"><path d="M6 0a4 4 0 0 0-4 4c0 3 4 8 4 8s4-5 4-8a4 4 0 0 0-4-4zm0 5.5A1.5 1.5 0 1 1 6 2.5a1.5 1.5 0 0 1 0 3z"/></svg>42 Quillmere Road, Teddington, Middlesex KT4 9RW</li>
      <li><svg viewBox="0 0 12 12"><path d="M2.5 0.5l2 2.5-1.2 1.4a7 7 0 0 0 4.3 4.3L9 7.5l2.5 2-1.3 2C5 11.5 0.5 7 0.5 1.8z"/></svg>T: 020 7946 0813</li>
      <li><svg viewBox="0 0 12 12"><rect x="3" y="0" width="6" height="12" rx="1.2"/></svg>M: 07700 900 412</li>
      <li><svg viewBox="0 0 12 12"><path d="M0 2h12v8H0zM1 3l5 4 5-4" stroke="#fff" stroke-width="0.8"/></svg>marnie@bramwelloakes.co.uk</li>
      <li><svg viewBox="0 0 12 12"><circle cx="6" cy="6" r="5.5"/></svg>www.bramwelloakes.co.uk</li>
    </ul>

    <div class="holder">
      <div class="holder-name">Marnie Thwaite</div>
      <div class="holder-role">Director</div>
    </div>
  </section>

  <section class="card card-back" aria-label="Business card back">
    <div class="back-web">www.bramwelloakes.co.uk</div>
    <div class="back-brand">
      <span class="brand-mark"></span>
      <span class="brand-name">Bramwell Oakes</span>
    </div>
  </section>

</main>
</body>
</html>
```